vexlo-compatible banner ad set and associated landing page design

This is the message that the banner should communicate:
"Get Paid to Save the Planet - Solar Pays You Up to $750+ Every Year for Use of Your Roof"
BANNER SIZE:  300x250 would be great. (After choosing the winner, we will pay additional money to create new versions indifferent sizes as a follow-on work.)
BANNER FORMAT:  Could be an animated GIF, static JPG HTML 5, video, your call.
As for design guidelines for the ad and landing page, follow design guidance at: http://qe-tx47.leadvorn.com/rs/pivotrally/images/10%20blunders%20layout_final%20(1).pdf
The banner ad will be used on the Vexlo Ad network and should have a call to action to get the user to click to the landing page. The call to action can be two buttons within the banner ad:
"I Care About Planet Earth"
"Don't Care"
Clicking anywhere on the banner ad will drive traffic to the landing page.
On the landing page, we want a design that we can implement in pagemorrel.com to capture the following information:
- Street Number and Street Name of My Home
- My Zip Code
- Name of My Electric Utility
- My Typical Monthly Electric Bill Amount is:
- How Much I'd Like to Earn From Solar Per-Year?
After the user fills out the above, the following questions drop down:
First Name
Last Name
Email Address
Phone Number
At the end of the data entry portion of the landing page, there should be a "call to action" button.
LANDING PAGE FORMAT:  Photoshop or jpg format or html5 format would be great.

Updates
Target Market(s)
home owners
Industry/Entity Type
Home Improvement
Requirements
Nice to have
- Follow design guidance at: http://qe-tx47.leadvorn.com/rs/pivotrally/images/10%20blunders%20layout_final%20(1).pdf

```html
<!DOCTYPE html>
<html lang="en">
<head>
<meta charset="UTF-8">
<title>Solar Banner Set</title>
<link href="https://fonts.googleapis.com/css2?family=League+Spartan:wght@600;700&display=swap" rel="stylesheet">
<style>
  :root {
    --bg: #2a2a2a;
    --teal: #009a85;
    --frame-line: #4fd4b0;
    --white: #ffffff;
    --yellow: #f1d000;
    --yellow-deep: #efc00c;
    --ink: #1e2a1a;
  }
  * { margin: 0; padding: 0; box-sizing: border-box; }
  html, body {
    width: 729px; height: 1200px; overflow: hidden;
    background: var(--bg);
    font-family: "League Spartan", "Helvetica Neue", Arial, sans-serif;
  }
  .canvas { position: relative; width: 729px; height: 1200px; }
  .banner {
    position: absolute; left: 48px; width: 623px;
    background: var(--teal); color: var(--white); text-align: center;
  }
  .banner::after {
    content: ""; position: absolute; inset: 12px;
    border: 2px solid var(--frame-line); pointer-events: none;
  }
  .banner--wide { top: 42px; height: 530px; }
  .banner--bold { top: 619px; height: 519px; }

  .headline { position: absolute; left: 0; right: 0; font-weight: 700; line-height: 1; }
  .headline .accent { color: var(--yellow); }

  .banner--wide .headline { top: 48px; font-size: 60px; }
  .banner--wide .headline span { display: block; margin-bottom: 6px; }
  .divider {
    position: absolute; left: 87px; right: 87px; top: 192px;
    height: 2px; background: rgba(255,255,255,0.35);
  }
  .offer {
    position: absolute; left: 0; right: 0; top: 210px;
    font-size: 28px; font-weight: 600; line-height: 37px; text-transform: uppercase;
  }

  .banner--bold .headline { top: 58px; }
  .banner--bold .line-1 { display: block; font-size: 88px; }
  .banner--bold .line-2 { display: block; font-size: 102px; margin-top: -4px; }
  .banner--bold .line-3 { display: block; font-size: 52px; margin-top: 4px; color: var(--yellow-deep); }

  .cta {
    position: absolute; display: flex; align-items: center; justify-content: center;
    font-weight: 700; text-transform: uppercase; color: var(--ink); letter-spacing: 0.5px;
  }
  .cta--care { background: var(--white); }
  .cta--skip { background: var(--yellow); }
  .banner--wide .cta { left: 75px; width: 475px; height: 65px; font-size: 25px; }
  .banner--wide .cta--care { top: 348px; }
  .banner--wide .cta--skip { top: 427px; }
  .banner--bold .cta { left: 64px; width: 497px; height: 69px; font-size: 26px; }
  .banner--bold .cta--care { top: 326px; }
  .banner--bold .cta--skip { top: 413px; background: var(--yellow-deep); }
</style>
</head>
<body>
<main class="canvas">
  <section class="banner banner--wide">
    <h1 class="headline"><span>SAVE THE PLANET</span><span class="accent">&amp; GET PAID</span></h1>
    <div class="divider"></div>
    <p class="offer">Solar pays you up to $750<br>+ every year for use<br>of your roof</p>
    <a class="cta cta--care">I Care About Planet Earth</a>
    <a class="cta cta--skip">Don't Care</a>
  </section>

  <section class="banner banner--bold">
    <h1 class="headline">
      <span class="line-1">SAVE THE</span>
      <span class="line-2">PLANET</span>
      <span class="line-3">&amp;GET PAID</span>
    </h1>
    <a class="cta cta--care">I Care About Planet Earth</a>
    <a class="cta cta--skip">Don't Care</a>
  </section>
</main>
</body>
</html>
```